Theater Production Company in Las Vegas

Needing a business card for a theater production company in Las Vegas. We are a full service theatrical production company specializing in Las Vegas entertainment, national
touring shows, and one-off events. From gorilla marketing teams to large scale productions... we do it,and better than anyone.

We like the feel of something hand made and organic.The final design should be creative and communicate that we specialize in theater and special events. We would like to have a design with a front and back.

Hi All,

I want to elaborate on the style of the design that we are hoping for. We are a theater production company in Las Vegas, so the competition is fierce and having a clever business card is incredibly important. 

I am attached a few concepts of a "feel" that would be nice to have conveyed in our card. We love the "worn and vintage" feel that is often seen in antique circus posters. Traditionally, the circus posters are clustered and full of copy - I want a more simplified version of that. Not so cluttered, but with that worn feel. Perhaps even having the card printed on recycled paper to give that textured feel to the visual. 

Example 1 - has a fun worn look, with stars. Some version of this for the back of the card would be fun.
Example 2 - Same things, cool worn feel. Perhaps a small star at the center of the swirl and a little softer on the "grunge".
Example 3 - Has the circus ornament but the colors are nice, not overpowering and again, has that worn feel.
Example 4 - This design isn't as "tight" and cluttered. Has some room to breathe.
Example 5 - I am really liking the look of the this and the above, especially for the back of the card. 

But just to reiterate, the front and face of the card needs to be clear and easy to read. 

Hi Designers, 

I have posted an update so you can have a clearer understanding of what we are needing. I have also increased the funding.

Thank you in advance for your help.

Brigid

Marketing

• We want to assign creative license. We are creative and hate to be limited by restrictions. Have fun!

The attached files are our logo. One of the files is a business card design that I love. Just a sample of our taste.
• We would like to incorporate: Purveyors of Performance
as our tagline. I like a vintage, worn feel to the look of designs. Just the word "purveyor" sounds vintage.

```html
<!DOCTYPE html>
<html lang="en">
<head>
<meta charset="utf-8">
<title>Lumen Hall Productions – Business Card</title>
<link href="https://fonts.googleapis.com/css2?family=Jost:wght@300;400&family=Oswald:wght@500&family=Arimo:wght@400&display=swap" rel="stylesheet">
<style>
  :root {
    --backdrop: #ece7e1;
    --card: #ffffff;
    --brush: #e2e2e2;
    --brush-light: #eeeeee;
    --mark-fade: #ececec;
    --ink: #1f1f1f;
    --ink-soft: #777777;
    --name-grey: #8c8c8c;
  }
  html, body {
    margin: 0;
    width: 1200px;
    height: 573px;
    overflow: hidden;
    background: var(--backdrop);
  }
  .stage {
    position: relative;
    width: 1200px;
    height: 573px;
  }
  .card {
    position: absolute;
    top: 27px;
    width: 292px;
    height: 515px;
    background: var(--card);
    box-shadow: 0 2px 6px rgba(0,0,0,.28);
    overflow: hidden;
  }
  .card--front { left: 316px; }
  .card--back  { left: 638px; }

  .brush-frame {
    position: absolute;
    inset: 0;
    width: 292px;
    height: 515px;
  }

  .faded-mark {
    position: absolute;
    left: -10px;
    top: 215px;
    width: 300px;
    height: 300px;
    background: radial-gradient(ellipse at 40% 55%, var(--mark-fade) 0%, rgba(236,236,236,.55) 40%, rgba(255,255,255,0) 70%);
  }

  .wordmark {
    position: absolute;
    left: 0;
    width: 100%;
    text-align: center;
    font-family: "Jost", sans-serif;
    font-weight: 400;
    color: var(--ink);
  }
  .wordmark__name {
    display: block;
    font-size: 44px;
    line-height: 1;
    letter-spacing: 1px;
  }
  .wordmark__sub {
    display: block;
    margin-top: 12px;
    font-size: 8px;
    letter-spacing: 13px;
    text-transform: uppercase;
    padding-left: 13px;
  }
  .card--front .wordmark { top: 113px; }
  .card--back .wordmark  { top: 222px; }

  .tagline {
    position: absolute;
    top: 192px;
    left: 0;
    width: 100%;
    text-align: center;
    font-family: "Jost", sans-serif;
    font-weight: 300;
    font-size: 17.5px;
    letter-spacing: 1px;
    color: var(--ink-soft);
    margin: 0;
  }

  .person {
    position: absolute;
    top: 340px;
    left: 17px;
  }
  .person__name {
    margin: 0;
    font-family: "Oswald", sans-serif;
    font-weight: 500;
    font-size: 15px;
    letter-spacing: .3px;
    text-transform: uppercase;
    color: var(--name-grey);
  }
  .person__title {
    margin: 0;
    font-family: "Arimo", sans-serif;
    font-size: 12.5px;
    color: var(--name-grey);
  }

  .contact {
    position: absolute;
    top: 340px;
    left: 150px;
    font-family: "Arimo", sans-serif;
    font-size: 14px;
    line-height: 19px;
    color: var(--ink);
    font-style: normal;
  }
  .contact__address { margin-top: 9px; }

  .web {
    position: absolute;
    top: 309px;
    left: 0;
    width: 100%;
    text-align: center;
    font-family: "Jost", sans-serif;
    font-weight: 400;
    font-size: 17px;
    letter-spacing: 3px;
    color: var(--ink-soft);
  }
</style>
</head>
<body>
<main class="stage">
  <section class="card card--front" aria-label="Card front">
    <svg class="brush-frame" viewBox="0 0 292 515" aria-hidden="true">
      <path fill="var(--brush)" fill-rule="evenodd" d="M0 0H292V515H0Z M6 5 L40 8 L70 4 L110 9 L150 5 L190 10 L230 4 L262 8 L286 5 L283 40 L288 80 L282 130 L287 170 L281 220 L286 270 L280 330 L287 380 L282 430 L288 470 L285 509 L250 506 L210 511 L170 505 L120 510 L80 504 L40 510 L7 507 L10 470 L4 430 L9 380 L3 330 L10 280 L5 230 L9 180 L4 130 L10 80 L5 40 Z"/>
      <g stroke="var(--brush-light)" stroke-width="2" stroke-linecap="round" fill="none">
        <path d="M14 14 L60 16 M120 15 L200 13 M240 16 L278 14"/>
        <path d="M278 60 L276 140 M277 250 L279 340 M276 420 L278 495"/>
        <path d="M16 500 L90 498 M150 501 L230 499"/>
        <path d="M15 90 L13 180 M14 300 L16 400"/>
      </g>
    </svg>
    <div class="faded-mark" role="img" aria-label="Faint brush-textured backdrop mark"></div>

    <div class="wordmark">
      <span class="wordmark__name">Lumen Hall</span>
      <span class="wordmark__sub">Productions</span>
    </div>
    <p class="tagline">Purveyors of Performance</p>

    <div class="person">
      <p class="person__name">Shannon Brigid</p>
      <p class="person__title">Title</p>
    </div>

    <address class="contact">
      <div>P : 000 000 0000</div>
      <div>F : 000 000 0000</div>
      <div>C: 000 000 0000</div>
      <div>www.lumenhall.com</div>
      <div class="contact__address">
        1st floor Apart<br>
        Street name<br>
        city name 123456
      </div>
    </address>
  </section>

  <section class="card card--back" aria-label="Card back">
    <svg class="brush-frame" viewBox="0 0 292 515" aria-hidden="true">
      <path fill="var(--brush)" fill-rule="evenodd" d="M0 0H292V515H0Z M5 6 L50 4 L90 9 L130 5 L170 10 L210 4 L250 9 L287 5 L282 50 L288 100 L281 150 L287 200 L280 260 L286 310 L281 360 L288 410 L282 460 L286 509 L240 505 L200 511 L160 506 L110 510 L70 505 L30 511 L6 507 L10 460 L4 410 L10 350 L3 300 L9 250 L4 200 L10 140 L3 90 L9 40 Z"/>
      <g stroke="var(--brush-light)" stroke-width="2" stroke-linecap="round" fill="none">
        <path d="M16 14 L80 16 M140 13 L220 15"/>
        <path d="M277 40 L279 120 M276 220 L278 320 M279 400 L277 490"/>
        <path d="M20 499 L100 501 M170 498 L260 500"/>
        <path d="M14 60 L16 160 M13 280 L15 380"/>
      </g>
    </svg>
    <div class="wordmark">
      <span class="wordmark__name">Lumen Hall</span>
      <span class="wordmark__sub">Productions</span>
    </div>
    <div class="web">www.lumenhall.com</div>
  </section>
</main>
</body>
</html>
```